Building Company Business Card Design

Need a design for a business card:
It needs to have: Name, Phone, Facebook link, Website, email
i would also like a list of works we undertake:
-New Homes
-Extensions, Renovations & Bathrooms
-Decking, Carports, Sheds (Residential and Industrial)
-Carpentry
-Fences, Patios & Pergolas

Name, Phone, Facebook link, Website, email + details of services provided listed in description

```html
<!DOCTYPE html>
<html lang="en">
<head>
<meta charset="utf-8">
<title>Ridgeline Homes – Business Card</title>
<link href="https://fonts.googleapis.com/css2?family=Montserrat:wght@400;500;600;700&family=Roboto+Condensed:wght@400&display=swap" rel="stylesheet">
<style>
  :root {
    --bg: #8c8d90;
    --card-dark: #000000;
    --card-light: #ffffff;
    --green: #3cbc55;
    --grey-text: #8a8a8a;
    --ink: #1c1c1c;
    --white: #ffffff;
  }
  * { margin: 0; padding: 0; box-sizing: border-box; }
  html, body { width: 1200px; height: 939px; overflow: hidden; }
  body {
    background: var(--bg);
    font-family: "Montserrat", sans-serif;
    position: relative;
  }
  .card {
    position: absolute;
    top: 315px;
    width: 540px;
    height: 309px;
    overflow: hidden;
    box-shadow: 0 8px 24px rgba(0,0,0,0.3);
  }
  .card--front { left: 40px; background: var(--card-dark); }
  .card--back { left: 620px; background: var(--card-light); color: var(--ink); }

  .brand {
    position: absolute;
    display: flex;
    align-items: center;
    gap: 12px;
  }
  .brand__mark { width: 30px; height: 30px; background: var(--green); flex: none; }
  .brand__name {
    font-weight: 600;
    text-transform: uppercase;
    line-height: 1.2;
    letter-spacing: 0.3px;
    white-space: nowrap;
  }
  .card--front .brand { left: 50%; top: 50%; transform: translate(-50%, -50%); }
  .card--front .brand__name { color: var(--white); font-size: 22px; }
  .card--front .brand__mark { width: 40px; height: 40px; }
  .card--back .brand { left: 40px; top: 112px; gap: 10px; }
  .card--back .brand__mark { width: 26px; height: 26px; }
  .card--back .brand__name { color: var(--ink); font-size: 13px; }

  .person { position: absolute; left: 335px; top: 30px; }
  .person__name { font-weight: 700; font-size: 20px; color: var(--grey-text); letter-spacing: 0.5px; white-space: nowrap; }
  .person__surname { color: var(--green); }
  .person__role { font-size: 11px; color: var(--ink); margin-top: 2px; }

  .contact { position: absolute; left: 335px; top: 100px; font-size: 11px; line-height: 1.5; white-space: nowrap; }
  .contact__address { margin-bottom: 12px; letter-spacing: 0.4px; }
  .contact__row { display: flex; align-items: center; gap: 6px; }
  .contact__row svg { width: 11px; height: 11px; flex: none; }
  .contact__social { margin-top: 10px; }
  .contact__dot { width: 11px; height: 11px; border-radius: 50%; background: var(--green); flex: none; }

  .services {
    position: absolute; left: 40px; top: 190px;
    list-style: none;
    font-family: "Roboto Condensed", sans-serif;
    font-size: 13px; line-height: 1.45;
    white-space: nowrap;
  }
  .services li { display: flex; align-items: center; gap: 8px; }
  .services li::before { content: ""; width: 7px; height: 7px; background: var(--green); flex: none; }
  .services small { font-size: 9px; }
</style>
</head>
<body>
  <section class="card card--front" aria-label="Card front">
    <div class="brand">
      <span class="brand__mark"></span>
      <span class="brand__name">Ridgeline Homes<br>and Developments Pty Ltd</span>
    </div>
  </section>

  <section class="card card--back" aria-label="Card back">
    <div class="person">
      <p class="person__name">DANIEL <span class="person__surname">REEVE</span></p>
      <p class="person__role">Owner</p>
    </div>

    <div class="brand">
      <span class="brand__mark"></span>
      <span class="brand__name">Ridgeline Homes<br>and Developments Pty Ltd</span>
    </div>

    <div class="contact">
      <p class="contact__address">12 Harlow Street,<br>Eastbrook, WA 6099</p>
      <p class="contact__row">
        <svg viewBox="0 0 24 24"><path fill="#3cbc55" d="M6.6 10.8a15 15 0 0 0 6.6 6.6l2.2-2.2c.3-.3.7-.4 1-.2 1.1.4 2.3.6 3.6.6.6 0 1 .4 1 1V20c0 .6-.4 1-1 1A17 17 0 0 1 3 4c0-.6.4-1 1-1h3.5c.6 0 1 .4 1 1 0 1.3.2 2.5.6 3.6.1.3 0 .7-.2 1z"/></svg>
        (08) 9400 2718
      </p>
      <p class="contact__row">
        <svg viewBox="0 0 24 24"><rect x="2" y="5" width="20" height="14" fill="#3cbc55"/><path d="M2 5l10 8 10-8" stroke="#fff" stroke-width="2" fill="none"/></svg>
        info@ridgelinehomes.com.au
      </p>
      <p class="contact__row">
        <svg viewBox="0 0 24 24" fill="none" stroke="#3cbc55" stroke-width="2"><circle cx="12" cy="12" r="9"/><path d="M3 12h18M12 3c3 3 3 15 0 18M12 3c-3 3-3 15 0 18"/></svg>
        www.ridgelinehomes.com.au
      </p>
      <p class="contact__row contact__social">
        <span class="contact__dot"></span>
        /ridgelinehomes
      </p>
    </div>

    <ul class="services">
      <li>New Homes</li>
      <li>Extensions, Renovations &amp; Bathrooms</li>
      <li>Decking, Carports, Sheds&nbsp;<small>(Residential and Industrial)</small></li>
      <li>Carpentry</li>
      <li>Fences, Patios &amp; Pergolas</li>
    </ul>
  </section>
</body>
</html>
```